Buch-/eBook-Cover für psychologische Beratung
Mirell hat sehr gut verstanden worauf es mir ankam und hat das Cover sehr gut auf das bereits bestehende abgestimmt. Sie hat zuverlässig geantwortet und Korrekturwünsche präzise ausgeführt. Grosses Kompliment! Gerne wieder.
Zielgruppe
psychologische Beratung, Zielgruppe Frauen
Aufgabenstellung
Es ist ein bestehendes ebook, das ich über meine frühere Website gekauft habe. Diese wird aufgelöst. Das ebook ist nun auf brixa und soll auch auf kolvento, aber offensichtlich zieht der Titel nicht. Deshalb möchte ich den ändern.
Der neue Titel und Untertitel lautet: Atmen statt zweifeln. Leises Naschen deuten, alte Muster entwirren.
Meine Idee wäre es, als Blickfang das Wort 'Atmen' und 'Leises Naschen' hervorzuheben.
Es ist mir wichtig, dass - vielleicht mit einer Andeutung eines Tellers - sofort klar wird, dass es um Essen geht.
Das Design soll passend zum Inhalt sein (Schrift und Illustrationen).
Das eBook ist im Querformat gehalten, weil es ein Arbeitsbuch ist. Für die Werbung brauche ich aber zusätzlich eine Version, die ins Hochformat passt.
Das Design darf nicht zu überladen sein.

```html
<!DOCTYPE html>
<html lang="de">
<head>
<meta charset="utf-8">
<title>Atmen statt zweifeln – Cover</title>
<link rel="stylesheet" href="https://fonts.googleapis.com/css2?family=Jost:wght@400;500;600&family=Sacramento&display=swap">
<style>
  :root {
    --stage: #e6e5ea;
    --paper: #ffffff;
    --cream: #fdedcc;
    --orange: #f29c3a;
    --ink: #333333;
    --line-art: #e9c592;
  }
  html, body {
    margin: 0;
    padding: 0;
    width: 675px;
    height: 1200px;
    overflow: hidden;
    background: var(--stage);
  }
  .canvas {
    position: relative;
    width: 675px;
    height: 1200px;
  }
  .cover {
    position: absolute;
    display: block;
    background: var(--paper);
  }
  .cover--landscape { left: 86px; top: 122px; width: 503px; height: 355px; }
  .cover--portrait  { left: 160px; top: 586px; width: 355px; height: 503px; }
  .title-script { font-family: "Sacramento", cursive; fill: var(--orange); }
  .title-line   { font-family: "Jost", sans-serif; font-weight: 400; fill: var(--ink); }
  .topic        { font-family: "Jost", sans-serif; font-weight: 600; }
  .subtitle     { font-family: "Jost", sans-serif; font-weight: 400; }
  .author       { font-family: "Jost", sans-serif; font-weight: 400; fill: var(--ink); }
  .format-label { font-family: "Jost", sans-serif; font-weight: 400; fill: var(--paper); }
  .illustration { fill: var(--line-art); opacity: 0.55; }
  .clover       { fill: var(--orange); opacity: 0.7; }
</style>
</head>
<body>
<div class="canvas">

  <!-- Querformat: Arbeitsbuch -->
  <svg class="cover cover--landscape" viewBox="0 0 503 355" xmlns="http://www.w3.org/2000/svg">
    <rect width="503" height="355" fill="var(--paper)"/>
    <path class="band-cream" fill="var(--cream)"
          d="M259 0 C225 20 218 60 236 110 C258 170 260 230 220 290 C200 320 180 340 159 355 L503 355 L503 0 Z"/>
    <path class="band-orange" fill="var(--orange)"
          d="M503 75 C430 100 380 150 320 215 C270 270 220 320 159 355 L503 355 Z"/>

    <rect class="illustration" role="img" aria-label="Einlinige Zeichnung: Gabel, Teller mit Herz und Messer"
          x="244" y="133" width="259" height="164" rx="8"/>
    <circle class="clover" role="img" aria-label="Kleines Kleeblatt-Ornament" cx="465" cy="40" r="15"/>

    <text class="title-script" x="38" y="101" font-size="72">Atmen</text>
    <text class="title-line" x="41" y="141" font-size="21">statt zweifeln.</text>
    <text class="topic" x="41" y="213" font-size="20" fill="var(--orange)">Leises</text>
    <text class="topic" x="41" y="241" font-size="20" fill="var(--orange)">Naschen</text>
    <text class="subtitle" x="41" y="260" font-size="15" fill="var(--ink)">deuten, alte</text>
    <text class="subtitle" x="41" y="279" font-size="15" fill="var(--ink)">Muster entwirren.</text>
    <text class="author" x="41" y="324" font-size="12.5">Selina Marwald</text>
    <text class="format-label" x="463" y="324" font-size="12.5" text-anchor="end">WorkBook</text>
  </svg>

  <!-- Hochformat: Werbung -->
  <svg class="cover cover--portrait" viewBox="0 0 355 503" xmlns="http://www.w3.org/2000/svg">
    <rect width="355" height="503" fill="var(--paper)"/>
    <path class="band-cream" fill="var(--cream)"
          d="M355 205 C300 215 270 270 220 310 C170 345 80 365 0 350 L0 503 L355 503 Z"/>
    <path class="band-orange" fill="var(--orange)"
          d="M0 352 C50 380 110 395 170 402 C240 412 300 425 355 445 L355 503 L0 503 Z"/>

    <rect class="illustration" role="img" aria-label="Einlinige Zeichnung: Gabel, Teller mit Herz und Messer"
          x="45" y="239" width="220" height="158" rx="8"/>
    <circle class="clover" role="img" aria-label="Kleines Kleeblatt-Ornament" cx="325" cy="320" r="13"/>

    <text class="author" x="177.5" y="36" font-size="12.5" text-anchor="middle">Selina Marwald</text>
    <text class="title-script" x="177.5" y="140" font-size="76" text-anchor="middle">Atmen</text>
    <text class="title-line" x="177.5" y="178" font-size="22" text-anchor="middle">statt zweifeln.</text>
    <text class="topic" x="177.5" y="455" font-size="19" fill="var(--paper)" text-anchor="middle">Leises Naschen</text>
    <text class="subtitle" x="177.5" y="474" font-size="14" fill="var(--paper)" text-anchor="middle">deuten, alte Muster entwirren.</text>
  </svg>

</div>
</body>
</html>
```